Business cards to promote my novel

Please create two designs for me.
Design 1. Business card.
Design 2. Bookmark
I want a design targeted towards people that like to read fiction, mystery novels. I would like to use colors that offset or complement my book cover, which I'm attaching as a file.
Design 1. Business cards
Design 2. Bookmarks
Target Market(s)
Mystery readers and book buyers
Industry/Entity Type
Publishing
Contact Information for Business Card
Design 1. I'd like my book cover on the front side along with: Coralie Vennet, Author
On the back side I'd like:
"Connect with me"
website https://coralievennet.example
Twitter @coralievennet
email coralievennet@mailbox.example
Design 2. Bookmark design size, 1.5" x 7". I'd like my book cover on the front
Font styles to use
Colors
Designer to choose colors to be used in the design.
Look and feel

```html
<!DOCTYPE html>
<html lang="en">
<head>
<meta charset="utf-8">
<title>Cold Ledger — Coralie Vennet, Author — Business Card</title>
<link rel="stylesheet" href="https://fonts.googleapis.com/css2?family=Bebas+Neue&family=Kaushan+Script&family=Oswald:wght@300;500;600&display=swap">
<style>
  :root {
    --canvas: #e9e6e1;
    --card-white: #f7f7f8;
    --ink: #1b2a2d;
    --teal: #1f9bab;
    --night: #0a1d20;
    --night-band: #0d2527;
    --photo-deep: #0b2326;
    --photo-mid: #1d5257;
    --photo-glow: #2f7d80;
    --title: #e6ecee;
    --band-text: #f2f4f4;
    --shadow: rgba(20, 18, 14, 0.22);
  }

  * { box-sizing: border-box; margin: 0; padding: 0; }

  html, body {
    width: 1200px;
    height: 800px;
    overflow: hidden;
    background: var(--canvas);
  }

  .stage {
    position: relative;
    width: 1200px;
    height: 800px;
  }

  /* ---------- Back side ---------- */
  .card-back {
    position: absolute;
    left: 70px;
    top: 240px;
    width: 560px;
    height: 320px;
    background: var(--card-white);
    box-shadow: 0 6px 18px var(--shadow);
    color: var(--ink);
  }

  .card-back__heading {
    position: absolute;
    top: 58px;
    left: 0;
    right: 0;
    text-align: center;
    font-family: "Kaushan Script", cursive;
    font-weight: 400;
    font-size: 50px;
    letter-spacing: 1px;
  }

  .contact {
    position: absolute;
    right: 40px;
    top: 176px;
    text-align: right;
    font-family: "Bebas Neue", sans-serif;
    font-size: 23px;
    line-height: 27px;
    letter-spacing: 0.6px;
    list-style: none;
  }

  .contact__icon {
    display: block;
    width: 22px;
    height: 22px;
    margin: 0 0 6px auto;
    border-radius: 50%;
    background: var(--teal);
  }

  /* ---------- Front side ---------- */
  .card-front {
    position: absolute;
    left: 760px;
    top: 120px;
    width: 320px;
    height: 560px;
    overflow: hidden;
    box-shadow: 0 6px 18px var(--shadow);
    background: var(--night);
  }

  .cover-photo {
    position: absolute;
    inset: 0 0 110px 0;
    background:
      radial-gradient(ellipse 70% 45% at 35% 70%, var(--photo-glow) 0%, transparent 70%),
      linear-gradient(180deg, var(--photo-deep) 0%, var(--photo-mid) 55%, var(--photo-deep) 100%);
  }

  .cover-title {
    position: absolute;
    left: 26px;
    right: 26px;
    bottom: 130px;
    font-family: "Oswald", sans-serif;
    font-weight: 500;
    font-size: 72px;
    line-height: 1.02;
    letter-spacing: 1px;
    color: var(--title);
    text-align: left;
    text-transform: uppercase;
  }

  .cover-title__line { display: block; }

  .author-band {
    position: absolute;
    left: 0;
    right: 0;
    bottom: 0;
    height: 110px;
    background: var(--night-band);
    padding: 18px 26px 0;
    color: var(--band-text);
  }

  .author-band__name {
    font-family: "Oswald", sans-serif;
    font-weight: 600;
    font-size: 33px;
    line-height: 40px;
    letter-spacing: 0.5px;
    text-transform: uppercase;
  }

  .author-band__role {
    font-family: "Oswald", sans-serif;
    font-weight: 300;
    font-size: 24px;
    line-height: 30px;
    letter-spacing: 1px;
    text-transform: uppercase;
  }
</style>
</head>
<body>
<main class="stage">

  <section class="card-back" aria-label="Business card back">
    <h2 class="card-back__heading">Connect with me</h2>
    <ul class="contact">
      <li><span class="contact__icon" aria-hidden="true"></span></li>
      <li class="contact__website">CORALIEVENNET.EXAMPLE</li>
      <li class="contact__handle">@CORALIEVENNET</li>
      <li class="contact__email">CORALIEVENNET@MAILBOX.EXAMPLE</li>
    </ul>
  </section>

  <section class="card-front" aria-label="Business card front">
    <div class="cover-photo" role="img" aria-label="Book cover photograph: a dark silhouetted figure walking through a misty teal night scene"></div>
    <h1 class="cover-title">
      <span class="cover-title__line">Cold</span>
      <span class="cover-title__line">Ledger</span>
    </h1>
    <div class="author-band">
      <p class="author-band__name">Coralie Vennet</p>
      <p class="author-band__role">Author</p>
    </div>
  </section>

</main>
</body>
</html>
```